www.dorvanpipeandboiler.com

I want everything on this page plus I need to add a ad that say save up to 20% on new installation.. also need to add a KTW logo sense I sing up with the KTW in San Diego CA. Just need this page to look more professional.
I had come to realize that I will need to convert the SPD file to HTML in order to upload to my site, so if any one is interested in doing the complete work let me know I know I need to raise my budget which I am working on that already. I had contacted support.
Remember for the header where you guys use picture, I be using my on pictures most likely a slide show of pictures so one design with different picture don't make different because I still will replaced it with my own. at my location in my industry the customer the faster they can see the phone number, the services and company experience the better.
New customers

```html
<!DOCTYPE html>
<html lang="en">
<head>
<meta charset="utf-8">
<title>Dorvan Pipe &amp; Boiler Inc.</title>
<link href="https://fonts.googleapis.com/css2?family=Arimo:wght@400;700&family=Merriweather:wght@400;700&display=swap" rel="stylesheet">
<style>
:root{
  --red:#862a2c;
  --red-dark:#7a2426;
  --orange:#f6a21a;
  --orange-deep:#ee8a06;
  --blue:#1a86c9;
  --blue-deep:#0f6fb0;
  --blue-light:#2b9de0;
  --text:#333;
  --muted:#555;
  --white:#fff;
}
*{margin:0;padding:0;box-sizing:border-box}
html,body{width:777px;height:1200px;overflow:hidden;background:#fff}
body{font-family:"Arimo",Arial,sans-serif;color:var(--text);position:relative}
.abs{position:absolute}
.serif{font-family:"Merriweather",Georgia,serif}

/* header */
.header{left:0;top:0;width:777px;height:102px;background:#fff}
.brand{left:44px;top:52px;width:170px;text-align:center;z-index:3}
.brand-mark{display:block;margin:0 auto 4px;width:14px;height:14px;border-radius:50%;background:var(--orange)}
.brand-name{font-weight:700;font-size:15px;line-height:17px;color:var(--red);letter-spacing:.3px}
.social{top:12px;display:flex;gap:8px;left:423px}
.social span{width:32px;height:32px;border-radius:4px;display:block}
.social .s1{background:#3b5a9a}.social .s2{background:#4fb9e8}.social .s3{background:#d9432f}.social .s4{background:#14628f}
.header-phone{left:605px;top:14px;display:flex;align-items:center;gap:6px}
.header-phone .lbl{font-size:12px;color:#333;line-height:14px}
.header-phone .num{font-size:16px;color:#222;line-height:18px}
.nav{top:76px;left:360px;display:flex;font-size:11px;color:#222}
.nav a{text-decoration:none;color:#222;padding:4px 10px;height:19px;line-height:12px}
.nav a.active{background:var(--blue-light);color:#fff;padding:4px 11px}

/* hero */
.hero{left:0;top:102px;width:777px;height:252px;background:radial-gradient(circle at 48% 50%,#3a66b8 0,#6a4a34 12%,#3b2e26 40%,#1e1a18 100%)}
.hero-caption{left:150px;top:316px;width:503px;height:22px;background:rgba(60,110,130,.75);color:#fff;font-size:17px;text-align:center;line-height:22px;letter-spacing:.3px}
.dots{left:367px;top:343px;display:flex;gap:3px}
.dots span{width:5px;height:5px;border-radius:50%;background:#fff}
.dots span:first-child{background:#888}

/* emergency band */
.band{left:0;top:354px;width:777px;height:68px;background:linear-gradient(#f9b52c,var(--orange-deep))}
.band p{left:44px;top:14px;width:520px;font-size:14px;line-height:20px;color:#fff}
.call-box{left:572px;top:366px;width:161px;height:45px;background:var(--blue);border-radius:3px;color:#fff;text-align:center}
.call-box .lbl{font-size:12px;line-height:14px;padding-top:5px}
.call-box .num{font-size:19px;line-height:22px}

/* welcome */
.welcome-h{left:44px;top:443px;font-size:16px;color:var(--red)}
.rule{height:0;border-top:1px dashed #ddd}
.welcome-rule{left:44px;top:468px;width:689px}
.welcome-p{left:44px;top:479px;width:690px;font-size:8.6px;line-height:15px;color:var(--muted)}
.welcome-p b{color:#333}

/* services */
.services{left:0;top:558px;width:777px;height:244px;background:var(--red)}
.services-h{left:43px;top:580px;font-size:15px;color:#fff}
.services-rule{left:43px;top:603px;width:430px;border-color:rgba(255,255,255,.25)}
.services-intro{left:44px;top:611px;width:450px;font-size:10.4px;line-height:17px;color:#fff}
.svc-list{font-size:10.4px;color:#fff;list-style:none}
.svc-list li{position:relative;padding-left:11px;height:26px;line-height:13px}
.svc-list li::before{content:"";position:absolute;left:0;top:3px;border-left:4px solid var(--orange);border-top:3px solid transparent;border-bottom:3px solid transparent}
.svc-a{left:44px;top:652px}
.svc-b{left:274px;top:652px}
.inquiry-h{left:552px;top:580px;font-size:12px;font-weight:700;color:#fff}
.inquiry-rule{left:552px;top:603px;width:181px;border-color:rgba(255,255,255,.25)}
.field{left:552px;width:151px;height:21px;background:rgba(255,255,255,.22);border-radius:2px;font-size:9px;font-style:italic;color:#fff;padding:5px 9px}
.submit{left:552px;top:762px;width:51px;height:18px;background:var(--orange);color:#fff;font-size:11px;font-weight:700;text-align:center;line-height:18px;border-radius:2px}

/* gallery */
.gallery-h{left:22px;top:819px;font-size:15px;color:var(--red)}
.gallery-rule{left:22px;top:842px;width:453px}
.arrows{left:452px;top:823px}
.thumb{top:850px;height:82px}
.thumb-cap{top:943px;font-size:10.4px;color:#222;text-align:center}
.promo{left:497px;top:832px;width:234px;height:130px;background:linear-gradient(#cfd5da,#8e979e)}
.promo-top{left:497px;top:832px;width:234px;height:22px;background:var(--blue);color:#fff;font-size:11px;font-weight:700;line-height:22px;padding-left:9px}
.promo-bot{left:497px;top:940px;width:234px;height:22px;background:rgba(26,134,201,.9);color:#fff;font-size:12px;font-weight:700;line-height:22px;padding-left:9px}

/* footer */
.footer{left:0;top:980px;width:777px;height:187px;background:linear-gradient(var(--blue-light),var(--blue-deep))}
.f-h{top:993px;font-size:11.5px;font-weight:700;color:#fff;padding-bottom:3px;border-bottom:1px dashed rgba(255,255,255,.5)}
.f-links{left:36px;top:1018px;list-style:none;font-size:10px;color:#fff}
.f-links li{height:21.4px}
.map{left:147px;top:1020px;width:194px;height:103px;border-radius:6px;background:linear-gradient(135deg,#e8ebe4,#d6dccf)}
.contact{left:373px;top:1026px;font-size:9.8px;color:#fff}
.contact .row{display:flex;position:absolute;left:0;white-space:nowrap}
.contact .k{width:22px;font-size:11px;font-weight:700}
.f-brand{left:580px;top:1050px;width:160px;text-align:center;color:rgba(255,255,255,.35);font-weight:700;font-size:15px;line-height:18px}
.f-brand i{display:block;margin:0 auto 8px;width:30px;height:30px;border-radius:50%;background:rgba(255,255,255,.25)}
.copy{left:0;top:1167px;width:777px;height:33px;background:var(--orange)}
.copy p{left:36px;top:1178px;font-size:9.6px;color:#333}
.accept{left:474px;top:1177px;font-size:10px;color:#333}
.cards{left:547px;top:1170px;display:flex;gap:4px}
.cards span{width:37px;height:24px;border-radius:3px;font-size:8px;font-weight:700;text-align:center;line-height:24px;color:#fff}
</style>
</head>
<body>

<div class="abs header"></div>
<div class="abs brand"><span class="brand-mark"></span><div class="brand-name">DORVAN PIPE<br>&amp; BOILER INC.</div></div>

<div class="abs social" aria-label="Social links">
  <span class="s1"></span><span class="s2"></span><span class="s3"></span><span class="s4" aria-label="KTW accredited badge"></span>
</div>

<div class="abs header-phone">
  <svg width="24" height="24" viewBox="0 0 24 24"><circle cx="12" cy="12" r="11" fill="none" stroke="#1a86c9" stroke-width="1.3"/><path d="M8 6c1 0 2 2 2 3s-1 1-1 2 2 4 3 4 1-1 2-1 3 1 3 2-1 2-2 2c-4 0-9-5-9-9 0-2 1-3 2-3z" fill="#1a86c9"/></svg>
  <div><div class="lbl">Call Us Today</div><div class="num">123 456 7890</div></div>
</div>

<nav class="abs nav">
  <a class="active">HOME</a><a>ABOUT US</a><a>SERVICES</a><a>WORK GALLERY</a><a>CONTACT US</a>
</nav>

<div class="abs hero" role="img" aria-label="Slideshow photo: plumber brazing a copper pipe with a torch"></div>
<div class="abs hero-caption serif">PROVIDING QUALITY WORK AT AFFORDABLE PRICES</div>
<div class="abs dots"><span></span><span></span><span></span></div>

<div class="abs band"><p class="abs serif">Our expert Emergency Maintenance teams are available 24 Hours 7 days a week, 365 days ayear to attend to your problems. Promptly &amp; competently!</p></div>
<div class="abs call-box"><div class="lbl">Call Us Today</div><div class="num">123 456 7890</div></div>

<h1 class="abs welcome-h serif" style="font-weight:400">Welcome to Dorvan Pipe &amp; Boiler</h1>
<div class="abs rule welcome-rule"></div>
<p class="abs welcome-p">Lorem ipsum dolor sit amet consectetur adipisicing elitsed do eiusmod tempor incididunt ut labore dolo magna aliqua. Ut enim ad minim veniam, quis nostrud exercitation ullamco laboris nisi ut aliquip ex comm consequat. Duis aute irure dolor in reprehenderit in voluptate velit esse cillum dolore eu fugiat nulla pariatur. Duis aute irure dolor in reprehenderit in voluptate velit esse cillum dolore eu fugiat nulla pariatur. Excepteur si occaecat cupidatat non proident, sunt in culpa qui officia deserunt mollit anim i reprehenderit in voluptate velit esse cillum dolore eu fugiat nulla pariatur. Excepteur si occaecat cupidatat non proiden<b>....Read More</b></p>

<section class="abs services"></section>
<h2 class="abs services-h serif" style="font-weight:400">Our Services</h2>
<div class="abs rule services-rule"></div>
<p class="abs services-intro">Ullamco laboris nisi ut aliquip ex comm consequat. Duis aute irure dolor in reprehend loreerit in voluptate velit esse cillum dolore eu fugiat nulla pariatur.</p>
<ul class="abs svc-list svc-a">
  <li>Water Heater Repair &amp; Installation</li><li>Boiler Repair &amp; Installation</li><li>Bathroom renovation</li><li>Kitchen Renovation</li><li>Water meters</li>
</ul>
<ul class="abs svc-list svc-b">
  <li>Gas Meters</li><li>Slab Leaks find and Repair</li><li>Water Piping Repair &amp; Installation</li><li>Repair/Replace/Install Plumbing Fixtures</li><li>Troubleshooting leaks in sinks, toilets,<br>faucets, bath tubs, sewer pipes</li>
</ul>
<div class="abs inquiry-h">Quick Inquiry</div>
<div class="abs rule inquiry-rule"></div>
<div class="abs field" style="top:614px">Name</div>
<div class="abs field" style="top:643px">Name</div>
<div class="abs field" style="top:672px">Email</div>
<div class="abs field" style="top:699px;height:56px">Message</div>
<div class="abs submit">Submit</div>

<h2 class="abs gallery-h serif" style="font-weight:400">Our Work Gallery</h2>
<div class="abs rule gallery-rule"></div>
<svg class="abs arrows" width="24" height="12" viewBox="0 0 24 12"><path d="M6 1 1 6l5 5M18 1l5 5-5 5" fill="none" stroke="#444" stroke-width="1.6"/></svg>
<div class="abs thumb" style="left:22px;width:144px;background:linear-gradient(120deg,#e4e9ee,#c7a49a)" role="img" aria-label="Technician servicing a wall boiler"></div>
<div class="abs thumb" style="left:186px;width:135px;background:linear-gradient(120deg,#b9c0c6,#c46a5a)" role="img" aria-label="Plumber with clipboard beside a heating manifold"></div>
<div class="abs thumb" style="left:331px;width:144px;background:linear-gradient(120deg,#dfe4e8,#6d7fa8)" role="img" aria-label="Plumber fixing pipes under a kitchen sink"></div>
<div class="abs thumb-cap" style="left:22px;width:144px">Lorem Isoum</div>
<div class="abs thumb-cap" style="left:186px;width:135px">Lorem Isoum</div>
<div class="abs thumb-cap" style="left:331px;width:144px">Lorem Isoum</div>

<div class="abs promo" role="img" aria-label="Photo of new drain pipe installation"></div>
<div class="abs promo-top serif">Save Up To 20% On New Installation</div>
<div class="abs promo-bot serif">Grab The Offer Today</div>

<footer class="abs footer"></footer>
<div class="abs f-h" style="left:36px">Quick Links</div>
<ul class="abs f-links"><li>HOME</li><li>ABOUT US</li><li>SERVICES</li><li>WORK GALLERY</li><li>CONTACT US</li></ul>
<div class="abs f-h" style="left:147px">Location Map</div>
<div class="abs map" role="img" aria-label="Street map of the shop location"></div>
<div class="abs f-h" style="left:373px">Contact Information</div>
<div class="abs contact">
  <div class="row" style="top:0"><span class="k">A:</span><span>Street Name, City Name<br>State Zipcode</span></div>
  <div class="row" style="top:46px"><span class="k">P:</span><span>123 456 7890</span></div>
  <div class="row" style="top:72px"><span class="k">TF:</span><span>1800 456 7890</span></div>
  <div class="row" style="top:98px"><span class="k">E:</span><span>inquiry@dorvanpipeandboiler.com</span></div>
</div>
<div class="abs f-brand"><i></i>DORVAN PIPE<br>&amp; BOILER INC.</div>

<div class="abs copy"></div>
<div class="copy"><p class="abs">Copyright ©2014, DorvanPipe&amp;Boiler &nbsp;All Rights Reserved</p></div>
<div class="abs accept">We Accept</div>
<div class="abs cards">
  <span style="background:#2a6fb4">Paynest</span><span style="background:#eee;color:#333">Orbix</span><span style="background:#fff;color:#1a3f8a">Veltra</span><span style="background:#4fa3d8">Amplio</span><span style="background:#c62a2a">Corvex</span>
</div>

</body>
</html>
```